Travel Group 'Lydgate Group' needs a new business card design

Lydgate Group is a diverse business specialising in bespoke, tailor made holidays to suit all budgets and we are specialists in planning exciting day/short trips to suit all markets. Our target market is very varied going from the corporate client and as well as people in the community who simply want to experience something special.
We are looking for a card design that will encourage people to look at our websites and social media platforms and to see for themselves the different facets to our business. It is essential that the card has social media icons for Facebook, Twitter and Instagram. We are looking for a card with a blank background with no pictures and for the front side to have the attached Lydgate logo. The card should have similar colour scheme to the attached Lydgate logo.
The card must have the following information on one side:
Maud Penrose
Business Development Manager
maudpenrose@lydgatevoyages.example
Lydgate Group, 87 Quarry Lane
Brackenford, Dunmoorshire, Scotland KA19 4TN
+44 (0)1632 960182
And then the card must have the following on the second side:
(Lydgate logo)
(social media icons)
www.lydgatevoyages.example
www.lydgateoutings.example
Target Market(s)
Our target market is very varied going from the corporate client and as well as people in the community who simply want to experience something special.
Industry/Entity Type
Business
Contact Information for Business Card
Maud Penrose
+44 (0)1632 960182
(Lydgate logo)
(social media icons)
www.lydgatevoyages.example
www.lydgateoutings.example
Requirements
Must have
- It is essential that the card has social media icons for Facebook, Twitter & Instagram.
Should not have
- Should not have any images other than Lydgate logo.

```html
<!DOCTYPE html>
<html lang="en">
<head>
<meta charset="utf-8">
<title>Lydgate Group – Business Card</title>
<link href="https://fonts.googleapis.com/css2?family=Arimo:wght@400;700&display=swap" rel="stylesheet">
<style>
  :root {
    --backdrop: #e9e6ea;
    --paper: #fbfbfc;
    --navy: #2a1e5c;
    --plum: #6a1f7a;
    --magenta: #c0137f;
    --ink: #2d2a3a;
    --muted: #4a4658;
    --white: #ffffff;
  }
  * { box-sizing: border-box; margin: 0; padding: 0; }
  html, body { width: 1200px; height: 1023px; overflow: hidden; }
  body {
    background: var(--backdrop);
    font-family: "Arimo", Arial, sans-serif;
    position: relative;
  }
  .card {
    position: absolute;
    width: 560px;
    height: 320px;
    border-radius: 26px;
    box-shadow: 0 6px 18px rgba(40, 20, 60, 0.18);
    overflow: hidden;
  }

  /* Front side */
  .card-front {
    left: 60px;
    top: 110px;
    background: var(--paper);
    color: var(--ink);
  }
  .front-address {
    position: absolute;
    right: 34px;
    top: 30px;
    text-align: right;
    font-size: 14px;
    font-style: normal;
    line-height: 1.35;
    color: var(--muted);
  }
  .front-rule {
    position: absolute;
    left: 34px;
    right: 34px;
    top: 100px;
    height: 1.5px;
    background: linear-gradient(90deg, var(--navy), var(--magenta));
  }
  .front-brand {
    position: absolute;
    left: 34px;
    top: 36px;
    display: flex;
    align-items: center;
    gap: 10px;
  }
  .brand-dot {
    width: 14px; height: 14px; border-radius: 50%;
    background: var(--magenta);
  }
  .brand-name {
    font-size: 30px;
    font-weight: 700;
    letter-spacing: 2px;
    color: var(--navy);
  }
  .person {
    position: absolute;
    left: 34px;
    top: 132px;
  }
  .person-name {
    font-size: 24px;
    color: var(--magenta);
    text-transform: uppercase;
    letter-spacing: 0.5px;
  }
  .person-role {
    font-size: 15px;
    color: var(--ink);
    margin-top: 4px;
  }
  .person-rule {
    margin-top: 12px;
    width: 260px;
    height: 1.5px;
    background: var(--navy);
  }
  .contact {
    position: absolute;
    left: 34px;
    bottom: 32px;
    list-style: none;
    font-size: 15px;
    color: var(--ink);
  }
  .contact li { display: flex; align-items: center; gap: 9px; margin-top: 6px; }
  .contact svg { width: 18px; height: 18px; flex: none; }

  /* Back side */
  .card-back {
    left: 580px;
    top: 590px;
    background: linear-gradient(160deg, var(--navy) 0%, var(--plum) 45%, var(--magenta) 100%);
    color: var(--white);
  }
  .back-brand {
    position: absolute;
    left: 0; right: 0;
    top: 110px;
    display: flex;
    justify-content: center;
    align-items: center;
    gap: 12px;
  }
  .back-brand .brand-dot { background: var(--white); }
  .back-brand .brand-name { color: var(--white); font-size: 40px; letter-spacing: 4px; }
  .back-footer {
    position: absolute;
    left: 0; right: 0;
    bottom: 30px;
    text-align: center;
    font-size: 13.5px;
    color: var(--white);
  }
  .social {
    display: flex;
    justify-content: center;
    gap: 8px;
    margin-bottom: 10px;
  }
  .social span {
    width: 16px; height: 16px; border-radius: 50%;
    background: var(--white);
    opacity: 0.9;
  }
</style>
</head>
<body>

  <section class="card card-front" aria-label="Card front">
    <div class="front-brand">
      <span class="brand-dot"></span>
      <span class="brand-name">LYDGATE</span>
    </div>
    <address class="front-address">
      Lydgate Group, 87 Quarry Lane<br>
      Brackenford, Dunmoorshire,<br>
      Scotland KA19 4TN
    </address>
    <div class="front-rule"></div>
    <div class="person">
      <p class="person-name">Maud Penrose</p>
      <p class="person-role">Business Development Manager</p>
      <div class="person-rule"></div>
    </div>
    <ul class="contact">
      <li>
        <svg viewBox="0 0 18 18" aria-hidden="true"><circle cx="9" cy="9" r="9" fill="#c0137f"/><path d="M6 5.2c.5-.4 1-.3 1.3.2l.7 1.3c.2.4.1.8-.2 1.1l-.4.3c.4.9 1.1 1.6 2 2l.3-.4c.3-.3.7-.4 1.1-.2l1.3.7c.5.3.6.8.2 1.3-.7.9-1.7 1-2.7.5C8 11.3 6.7 10 6 8.4c-.5-1-.6-2.3 0-3.2z" fill="#fff"/></svg>
        +44 (0)1632 960182
      </li>
      <li>
        <svg viewBox="0 0 18 18" aria-hidden="true"><circle cx="9" cy="9" r="9" fill="#c0137f"/><rect x="4.5" y="6" width="9" height="6.5" rx="0.8" fill="none" stroke="#fff" stroke-width="1.1"/><path d="M4.8 6.4 9 9.7l4.2-3.3" fill="none" stroke="#fff" stroke-width="1.1"/></svg>
        maudpenrose@lydgatevoyages.example
      </li>
    </ul>
  </section>

  <section class="card card-back" aria-label="Card back">
    <div class="back-brand">
      <span class="brand-dot"></span>
      <span class="brand-name">LYDGATE</span>
    </div>
    <div class="back-footer">
      <div class="social" aria-label="Social media links">
        <span></span><span></span><span></span>
      </div>
      <p>www.lydgatevoyages.example &nbsp;|&nbsp; www.lydgateoutings.example</p>
    </div>
  </section>

</body>
</html>
```